New Flyer Design Project - for sale units at The Lodge phase 3

on attached the A2 is full kitchen 1 bedroom, the A3 is gally kitchen and the B2 is the the 2 bedroom, on attached pictures the room with 2 queen beds is only for the 2 bedroom

This is going to be used to sale the units (real estate sale) so the layout could possibly be text and then pictures maybe 1 bedroom on one side and 2 on the back?

Experience the Modern Luxury of the New Phase 3 Building of the
Lodge at Harlow Bend

* Opening Spring 2019

* America's #17 Family Resort; Tennessee's Only Ranked Resort

1 Bedroom Bunk Suite (Galley Kitchen) - $199,000; Sleeps 6

* Private King Master Bedroom

* Bunk Bed Galley

* Granite Counters Throughout

* Fully Furnished with Custom Furnishings

* Private Balcony

* Equipped Galley Kitchen

* In Unit Laundry

* Queen Sleeper Sofa

1 Bedroom Bunk Suite (Full Kitchen) - $209,000; Sleeps 6

* Bunk Bed Galley

* Granite Counters throughout

* Equipped Full Kitchen

* Completely Furnished with Custom Furnishings

* Private Balcony

* In Unit Laundry

* Queen Sleeper Sofa

2 Bedroom Bunk Suite (Full Kitchen) - $249,000; Sleeps 10

* Private King Master Bedroom with On-Suite Bathroom

* Two Queen Bedroom

* Bunk Bed Galley

* Full Kitchen

* Private Balcony

* In Unit Laundry

* Queen Sleeper Sofa

Target Market(s)

people wanting to buy units in phase 3 of The Lodge at Harlow Bend

Industry/Entity Type

Real Estate Development

Requirements
Must have
• attached text to describe units and price
• pictures and layouts
• Contact Dale Porter
• 865-730-2958 Dale@brightfernretreats.example
Nice to have
• brand and logo
Should not have
• it should not be plain this is m ore of a luxury project

```html
<!DOCTYPE html>
<html lang="en">
<head>
<meta charset="utf-8">
<title>The Lodge at Harlow Bend — Phase 3 Unit Flyers</title>
<link rel="stylesheet" href="https://fonts.googleapis.com/css2?family=Roboto:wght@400;500;700&display=swap">
<style>
  :root {
    --backdrop: #939394;
    --paper: #ffffff;
    --slate: #5f5f5f;
    --charcoal: #2b2b2b;
    --teal: #5e8a90;
    --amber: #d9a05b;
    --heading: #3d5358;
    --ink: #2a2a2a;
    --photo-a: #c9cf9a;
    --photo-b: #8f8a78;
    --plan-frame: #3b2a26;
    --plan-fill: #cfc6b4;
  }
  * { box-sizing: border-box; margin: 0; padding: 0; }
  html, body { width: 1200px; height: 1200px; overflow: hidden; }
  body {
    background: var(--backdrop);
    font-family: "Roboto", Arial, sans-serif;
    color: var(--ink);
    position: relative;
  }
  .flyer {
    position: absolute;
    top: 219px;
    width: 491px;
    height: 689px;
    background: var(--paper);
    overflow: hidden;
  }
  .flyer--front { left: 100px; }
  .flyer--back { left: 644px; }
  .abs { position: absolute; }

  .top-rule { left: 0; top: 0; width: 308px; height: 7px; background: #555; }
  .room-photo {
    background: linear-gradient(160deg, var(--photo-a) 0%, #e9e6d6 45%, var(--photo-b) 100%);
  }
  .caption {
    left: 0; top: 309px; width: 308px; height: 67px;
    background: var(--teal); color: #fff;
    font-size: 13.4px; font-weight: 500; line-height: 16.5px;
    padding: 10px 18px; text-align: justify;
  }
  .brand {
    left: 320px; top: 25px; width: 148px; height: 96px;
    display: flex; align-items: center; justify-content: center; gap: 7px;
    color: var(--heading); font-size: 19px; font-weight: 700; text-align: center; line-height: 1.1;
  }
  .brand__dot { width: 12px; height: 12px; border-radius: 50%; background: var(--amber); flex: none; }

  .title-box {
    left: 311px; top: 148px; width: 166px; height: 125px;
    background: var(--slate); color: #fff; text-align: center;
    display: flex; flex-direction: column; justify-content: center;
  }
  .title-box__main { font-size: 31px; font-weight: 700; line-height: 1.05; }
  .title-box__sub { font-size: 21px; line-height: 1.25; }
  .price-box {
    left: 311px; top: 279px; width: 166px; height: 97px;
    background: var(--amber); color: #fff; text-align: center;
    display: flex; flex-direction: column; justify-content: center;
  }
  .price-box__price { font-size: 38px; font-weight: 700; line-height: 1.1; }
  .price-box__sleeps { font-size: 18px; }

  .provide-heading { font-size: 19px; font-weight: 700; color: var(--heading); }
  .features { list-style: none; }
  .features li { position: relative; padding-left: 17px; }
  .features li svg { position: absolute; left: 0; top: 2px; width: 11px; height: 11px; }
  .features--front { left: 28px; top: 424px; width: 230px; font-size: 12px; line-height: 14.5px; }
  .features--front li { margin-bottom: 14.3px; }

  .floor-plan { background: var(--plan-fill); }
  .floor-plan--front { left: 266px; top: 414px; width: 203px; height: 223px; border: 6px solid var(--plan-frame); }

  .footer { left: 0; top: 657px; width: 491px; height: 32px; background: var(--charcoal); color: #fff; }
  .footer__tab { left: 0; top: 0; height: 32px; width: 126px; }
  .footer__name { left: 24px; top: 6px; font-size: 16px; font-weight: 700; color: #fff; }
  .footer__phone { left: 154px; top: 7px; font-size: 13px; font-weight: 500; display: flex; align-items: center; gap: 3px; }
  .footer__web { left: 284px; top: 9px; font-size: 9px; letter-spacing: 0.6px; display: flex; align-items: center; gap: 6px; }
  .footer__web::before { content: ""; width: 4px; height: 3px; background: #fff; }

  .offer-box {
    background: var(--amber); color: #fff; text-align: center; font-weight: 500;
  }
  .offer-box__title { font-size: 17.5px; line-height: 21px; }
  .offer-box__price { font-size: 20px; font-weight: 700; }
  .offer-box--one { left: 246px; top: 13px; width: 232px; height: 94px; padding-top: 1px; }
  .offer-box--one .offer-box__price { margin-top: 9px; }
  .offer-box--two { left: 16px; top: 374px; width: 232px; height: 86px; padding-top: 7px; }
  .offer-box--two .offer-box__price { margin-top: 5px; }

  .features--one { left: 267px; top: 149px; width: 215px; font-size: 11.8px; line-height: 14.5px; }
  .features--one li { margin-bottom: 6.3px; }
  .features--two { left: 32px; top: 490px; width: 215px; font-size: 11.2px; line-height: 13.6px; }
  .features--two li { margin-bottom: 4px; }
  .features li.gap { margin-bottom: 8px; }
  .features li.plain { padding-left: 17px; }

  .floor-plan--one { left: 0; top: 162px; width: 246px; height: 177px; border: 1px solid #8a8a8a; background: #fff; }
  .floor-plan--one .floor-plan__inner { position: absolute; left: 32px; top: 10px; width: 190px; height: 158px; background: var(--plan-fill); border: 3px solid var(--plan-frame); }
  .floor-plan--two { left: 248px; top: 373px; width: 228px; height: 272px; border: 3px solid var(--plan-frame); }
</style>
</head>
<body>

<svg width="0" height="0" style="position:absolute">
  <defs>
    <symbol id="tick" viewBox="0 0 12 12">
      <circle cx="6" cy="6" r="6" fill="#1f1f1f"/>
      <path d="M3.2 6.2 L5.2 8.1 L8.9 4" fill="none" stroke="#fff" stroke-width="1.6"/>
    </symbol>
    <symbol id="phone" viewBox="0 0 12 12">
      <path d="M2.5 1 L4.5 1 L5.3 3.6 L4 4.7 C4.7 6.2 5.8 7.3 7.3 8 L8.4 6.7 L11 7.5 L11 9.5 C11 10.4 10.3 11 9.4 11 C5 10.7 1.3 7 1 2.6 C1 1.7 1.6 1 2.5 1 Z" fill="#fff"/>
    </symbol>
  </defs>
</svg>

<!-- Front: 1 Bedroom Bunk Suite (Galley Kitchen) -->
<section class="flyer flyer--front">
  <div class="abs top-rule"></div>
  <div class="abs room-photo" style="left:0;top:7px;width:308px;height:302px" role="img" aria-label="Photo of the king master bedroom with white bedding, green walls and bedside lamps"></div>
  <p class="abs caption">Experience the Modern Luxury of the New Phase 3 Building of the Lodge at Harlow Bend</p>

  <div class="abs brand"><span class="brand__dot"></span><span>The Lodge<br>at Harlow Bend</span></div>

  <div class="abs title-box">
    <div class="title-box__main">1 Bedroom</div>
    <div class="title-box__sub">Bunk Suite</div>
    <div class="title-box__sub">(Galley Kitchen)</div>
  </div>
  <div class="abs price-box">
    <div class="price-box__price">$199,000</div>
    <div class="price-box__sleeps">Sleeps 6</div>
  </div>

  <h2 class="abs provide-heading" style="left:22px;top:386px">What we provide</h2>
  <ul class="abs features features--front">
    <li><svg><use href="#tick"/></svg>Private King Master Bedroom</li>
    <li><svg><use href="#tick"/></svg>Bunk Bed Galley</li>
    <li><svg><use href="#tick"/></svg>Granite Counters Throughout</li>
    <li><svg><use href="#tick"/></svg>Fully Furnished with Custom Furnish-ings</li>
    <li><svg><use href="#tick"/></svg>Private Balcony</li>
    <li><svg><use href="#tick"/></svg>Equipped Galley Kitchen</li>
    <li><svg><use href="#tick"/></svg>In Unit Laundry</li>
  </ul>

  <div class="abs floor-plan floor-plan--front" role="img" aria-label="Floor plan of the 1 bedroom galley kitchen suite"></div>

  <footer class="abs footer">
    <svg class="abs footer__tab" viewBox="0 0 126 32" preserveAspectRatio="none"><polygon points="0,0 108,0 126,16 108,32 0,32" fill="var(--teal)"/><polyline points="108,0 126,16 108,32" fill="none" stroke="#fff" stroke-width="1"/></svg>
    <span class="abs footer__name">Dale Porter</span>
    <span class="abs footer__phone"><svg width="9" height="9"><use href="#phone"/></svg>865-730-2958</span>
    <span class="abs footer__web">brightfernretreats.example</span>
  </footer>
</section>

<!-- Back: 1 Bedroom (Full Kitchen) and 2 Bedroom -->
<section class="flyer flyer--back">
  <div class="abs room-photo" style="left:0;top:0;width:246px;height:158px" role="img" aria-label="Photo of the master bedroom with white bedding and green curtains"></div>

  <div class="abs offer-box offer-box--one">
    <div class="offer-box__title">1 Bedroom Bunk Suite<br>(Full Kitchen)</div>
    <div class="offer-box__price">$209,000; Sleeps 6</div>
  </div>

  <h2 class="abs provide-heading" style="left:267px;top:119px">What we provide</h2>
  <ul class="abs features features--one">
    <li><svg><use href="#tick"/></svg>Private King Master Bedroom</li>
    <li><svg><use href="#tick"/></svg>Bunk Bed Galley</li>
    <li><svg><use href="#tick"/></svg>Granite Counters throughout</li>
    <li class="gap"><svg><use href="#tick"/></svg>Equipped Full Kitchen</li>
    <li><svg><use href="#tick"/></svg>Completely Furnished with Custom Furnishings</li>
    <li><svg><use href="#tick"/></svg>Private Balcony</li>
    <li><svg><use href="#tick"/></svg>In Unit Laundry</li>
    <li><svg><use href="#tick"/></svg>Queen Sleeper Sofa</li>
  </ul>

  <div class="abs floor-plan--one">
    <div class="floor-plan__inner" role="img" aria-label="Floor plan of the 1 bedroom full kitchen suite"></div>
  </div>

  <div class="abs offer-box offer-box--two">
    <div class="offer-box__title">2 Bedroom Bunk Suite<br>(Full Kitchen)</div>
    <div class="offer-box__price">$249,000; Sleeps 10</div>
  </div>

  <h2 class="abs provide-heading" style="left:30px;top:464px">What we provide</h2>
  <ul class="abs features features--two">
    <li><svg><use href="#tick"/></svg>Two Queen Bedroom</li>
    <li><svg><use href="#tick"/></svg>Bunk Bed Galley</li>
    <li style="margin-bottom:0"><svg><use href="#tick"/></svg>Granite Counters Throughout</li>
    <li class="plain gap">Full Kitchen</li>
    <li class="gap"><svg><use href="#tick"/></svg>Completely Furnished with Custom Furnishings</li>
    <li><svg><use href="#tick"/></svg>Private Balcony</li>
    <li><svg><use href="#tick"/></svg>In Unit Laundry</li>
    <li><svg><use href="#tick"/></svg>Queen Sleeper Sofa</li>
  </ul>

  <div class="abs floor-plan floor-plan--two" role="img" aria-label="Floor plan of the 2 bedroom full kitchen suite"></div>

  <footer class="abs footer">
    <svg class="abs footer__tab" viewBox="0 0 126 32" preserveAspectRatio="none"><polygon points="0,0 108,0 126,16 108,32 0,32" fill="var(--teal)"/><polyline points="108,0 126,16 108,32" fill="none" stroke="#fff" stroke-width="1"/></svg>
    <span class="abs footer__name">Dale Porter</span>
    <span class="abs footer__phone"><svg width="9" height="9"><use href="#phone"/></svg>865-730-2958</span>
    <span class="abs footer__web">brightfernretreats.example</span>
  </footer>
</section>

</body>
</html>
```